Business Card Design Project

I have just chosen a logo and would now like this designed onto a business card for my hair salon. I would like it to be classy not to busy and have a wow factor when people look at them
Has to Include on card:
Logo Design
And business details below
Kellie-ann Drummond (owner)
0482 736 219
Rdw@vomblet.com.au
71 Willowmere Rise Corvin Cove
Logo is now attached please provide designs
Hair

```html
<!DOCTYPE html>
<html lang="en">
<head>
<meta charset="utf-8">
<title>Marlowe Hair Studio – Business Card</title>
<link rel="stylesheet" href="https://fonts.googleapis.com/css2?family=Cinzel:wght@400&family=Roboto+Condensed:wght@400&display=swap">
<style>
  :root {
    --backdrop-light: #7a4328;
    --backdrop-dark: #4a2a22;
    --card: #ebe7ce;
    --card-edge: #e2ddc0;
    --art: #d5d1b3;
    --band-top: #ffffff;
    --band-bottom: #f1efe2;
    --band-shadow: rgba(120, 110, 70, 0.18);
    --brand: #e0197d;
    --contact: #6e6b2c;
  }
  * { margin: 0; padding: 0; box-sizing: border-box; }
  html, body {
    width: 1200px;
    height: 925px;
    overflow: hidden;
  }
  body {
    position: relative;
    background: radial-gradient(ellipse at 50% 55%, var(--backdrop-light) 0%, var(--backdrop-dark) 100%);
  }
  .card {
    position: absolute;
    background: var(--card);
    border-radius: 36px;
    overflow: hidden;
    box-shadow: 0 14px 30px rgba(30, 12, 6, 0.45);
  }
  .card-front { left: 160px; top: 228px; width: 300px; height: 470px; }
  .card-back { left: 530px; top: 312px; width: 490px; height: 300px; }

  .hair-art {
    position: absolute;
    background: radial-gradient(ellipse at 50% 45%, var(--art) 0%, var(--art) 55%, var(--card) 100%);
    border-radius: 40%;
  }
  .card-front .hair-art { left: 22px; top: 40px; width: 256px; height: 270px; }
  .card-back .hair-art { left: 90px; top: 14px; width: 300px; height: 160px; }

  .band {
    position: absolute;
    left: 0;
    right: 0;
    background: linear-gradient(180deg, var(--band-top) 0%, var(--band-bottom) 100%);
    box-shadow: 0 10px 12px -6px var(--band-shadow);
  }
  .card-front .band { top: 318px; height: 90px; }
  .card-back .band { top: 170px; height: 86px; }

  .brand {
    position: absolute;
    left: 0; right: 0; top: 14px;
    text-align: center;
    font-family: "Cinzel", "Times New Roman", serif;
    font-weight: 400;
    color: var(--brand);
    line-height: 1;
  }
  .brand-main { display: block; font-size: 40px; letter-spacing: 1px; }
  .brand-sub { display: block; font-size: 20px; letter-spacing: 2px; margin-top: 6px; }

  .contact {
    position: absolute;
    left: 170px;
    top: 8px;
    list-style: none;
    font-family: "Roboto Condensed", "Arial Narrow", sans-serif;
    font-size: 15px;
    line-height: 18px;
    color: var(--contact);
  }
</style>
</head>
<body>
  <section class="card card-front" aria-label="Business card front">
    <div class="hair-art" role="img" aria-label="Faint illustration of a woman with long flowing hair"></div>
    <div class="band">
      <div class="brand">
        <span class="brand-main">MARLOWE</span>
        <span class="brand-sub">HAIR STUDIO</span>
      </div>
    </div>
  </section>

  <section class="card card-back" aria-label="Business card back">
    <div class="hair-art" role="img" aria-label="Faint illustration of a woman with long flowing hair"></div>
    <div class="band">
      <ul class="contact">
        <li>Kellie-ann Drummond</li>
        <li>+ 0482 736 219</li>
        <li>Rdw@vomblet.com.au</li>
        <li>71 Willowmere Rise Corvin Cove.</li>
      </ul>
    </div>
  </section>
</body>
</html>
```